HollowbrookJoinery (Custom Interior Trim work & Millwork Division)

HollowbrookJoinery

Cabinetry & Interior Finish

We are a custom millwork shop and fabricate cabinets, mantles, media rooms, bookcases, cabinet doors, dovetail draws, etc.

Also specialize in interior finish work (crown molding, trim work, staircases, installing kitchens, etc.

In the 2nd image only use if you can get the light fixture out of the picture thank you

please visit my web sites to get more pics and ideas.

you can copy and paste text and pics

www.qmaplerinc.example

www.hollowbrookjoinery.example

I like the color green tied into this project somehow

Shop

Serif

9bcb3c
ffffff
000000

• needs to be professional
• look and feel correct
• I added colors I would like to see but please feel free to add and be creative
• thank you
• Phone number
• email
• pics
• A picture of myself
• go to my website and copy it
• www.hollowbrookjoinery.example
• If this comes out right I will award the winner a web page design for my company

```html
<!DOCTYPE html>
<html lang="en">
<head>
<meta charset="utf-8">
<title>HollowbrookJoinery Flyer</title>
<link href="https://fonts.googleapis.com/css2?family=Roboto+Condensed:wght@400;700&family=Oswald:wght@500&display=swap" rel="stylesheet">
<style>
  :root {
    --green: #9bcb3c;
    --green-bright: #3fae2a;
    --green-deep: #2c8a20;
    --black: #000000;
    --white: #ffffff;
    --stage: #e4e4e4;
  }
  html, body {
    margin: 0;
    width: 1200px;
    height: 1000px;
    overflow: hidden;
    background: var(--stage);
  }
  .flyer {
    position: absolute;
    left: 267px;
    top: 31px;
    width: 495px;
    height: 698px;
    transform: scale(1.343);
    transform-origin: 0 0;
    background: var(--black);
    overflow: hidden;
    font-family: "Roboto Condensed", "Arial Narrow", sans-serif;
    color: var(--white);
    box-shadow: 0 4px 14px rgba(0,0,0,.35);
  }
  .flyer-shapes { position: absolute; inset: 0; }
  .intro {
    position: absolute;
    left: 20px;
    top: 44px;
    margin: 0;
    font-size: 9.5px;
    line-height: 13px;
  }
  .brand {
    position: absolute;
    right: 10px;
    top: 30px;
    text-align: right;
  }
  .brand-name {
    display: flex;
    align-items: center;
    justify-content: flex-end;
    gap: 4px;
    font-size: 12.5px;
    font-weight: 700;
    color: var(--green);
    letter-spacing: .2px;
  }
  .brand-mark { width: 8px; height: 8px; background: var(--green); }
  .brand-tagline { font-size: 6.5px; margin-top: 1px; }
  .greeting {
    position: absolute;
    right: 20px;
    top: 196px;
    margin: 0;
    font-family: "Oswald", "Roboto Condensed", sans-serif;
    font-weight: 500;
    font-size: 19px;
  }
  .about {
    position: absolute;
    right: 20px;
    top: 230px;
    width: 244px;
    margin: 0;
    font-size: 9.3px;
    line-height: 14.6px;
    text-align: right;
  }
  .offer {
    position: absolute;
    left: 150px;
    top: 325px;
    margin: 0;
    font-size: 9.3px;
    line-height: 14.6px;
  }
  .contact {
    position: absolute;
    left: 150px;
    top: 402px;
    margin: 0;
    font-size: 9.3px;
    line-height: 13px;
    font-weight: 700;
    text-shadow: 0 1px 2px rgba(0,0,0,.7);
  }
  .contact-lead { margin-bottom: 10px; display: block; }
</style>
</head>
<body>
<main class="flyer">
  <svg class="flyer-shapes" viewBox="0 0 495 698" width="495" height="698" aria-hidden="false">
    <defs>
      <linearGradient id="band-fill" x1="0" y1="0" x2="1" y2="1">
        <stop offset="0" stop-color="#46b22f"/>
        <stop offset="1" stop-color="#2c8a20"/>
      </linearGradient>
      <linearGradient id="photo-drawers" x1="0" y1="0" x2="1" y2="1">
        <stop offset="0" stop-color="#8e8e8a"/>
        <stop offset=".55" stop-color="#a4a4a0"/>
        <stop offset="1" stop-color="#3a3a38"/>
      </linearGradient>
      <linearGradient id="photo-light" x1="0" y1="0" x2="1" y2="1">
        <stop offset="0" stop-color="#f1efe9"/>
        <stop offset="1" stop-color="#a9a59c"/>
      </linearGradient>
      <linearGradient id="photo-stairs" x1="0" y1="0" x2="1" y2="1">
        <stop offset="0" stop-color="#e8e4dc"/>
        <stop offset="1" stop-color="#8b6d4e"/>
      </linearGradient>
      <linearGradient id="photo-dark" x1="0" y1="0" x2="1" y2="1">
        <stop offset="0" stop-color="#d8d6d0"/>
        <stop offset="1" stop-color="#3e3934"/>
      </linearGradient>
      <linearGradient id="photo-yellow" x1="0" y1="0" x2="1" y2="1">
        <stop offset="0" stop-color="#c9d43a"/>
        <stop offset="1" stop-color="#8a6a3c"/>
      </linearGradient>
      <linearGradient id="photo-grey" x1="0" y1="0" x2="1" y2="1">
        <stop offset="0" stop-color="#d9d4cb"/>
        <stop offset="1" stop-color="#7b6f60"/>
      </linearGradient>
      <linearGradient id="photo-media" x1="0" y1="0" x2="1" y2="1">
        <stop offset="0" stop-color="#d07a45"/>
        <stop offset="1" stop-color="#4a2f22"/>
      </linearGradient>
    </defs>

    <polygon class="corner-green" points="0,0 260,0 0,260" fill="var(--green-bright)"/>
    <polygon class="accent-green" points="0,270 40,310 0,350" fill="var(--green-bright)"/>

    <polygon class="tile" role="img" aria-label="Photo: white fireplace surround with built-in shelving" points="305,-35 400,60 305,155 210,60" fill="url(#photo-light)"/>
    <polygon class="tile" role="img" aria-label="Photo: white staircase with wood handrail" points="204,66 299,161 204,256 109,161" fill="url(#photo-stairs)"/>
    <polygon class="tile" role="img" aria-label="Photo: kitchen cabinetry with glass-front wine fridge" points="103,167 198,262 103,357 8,262" fill="url(#photo-dark)"/>

    <polygon class="feature-band" points="395,75 495,175 495,383 87,383" fill="url(#band-fill)"/>

    <polygon class="feature-photo" role="img" aria-label="Photo: the owner standing in front of white cabinet drawers with dark pulls" points="40,390 495,390 495,698 348,698" fill="url(#photo-drawers)"/>

    <polygon class="tile" role="img" aria-label="Photo: breakfast nook with yellow-green walls and window" points="0,360 80,440 0,520 -80,440" fill="url(#photo-yellow)"/>
    <polygon class="tile" role="img" aria-label="Photo: built-in cabinet wall with wainscoting" points="86,446 166,526 86,606 6,526" fill="url(#photo-grey)"/>
    <polygon class="tile" role="img" aria-label="Photo: built-in media centre in warm wood tones" points="172,532 252,612 172,692 92,612" fill="url(#photo-media)"/>
    <polygon class="tile" role="img" aria-label="Photo: built-in cabinetry detail" points="258,618 338,698 258,778 178,698" fill="url(#photo-grey)"/>
    <polygon class="accent-green" points="0,532 80,612 0,692 -80,612" fill="var(--green-bright)"/>
  </svg>

  <p class="intro">Ridgewell Builders Inc. is<br>located in Millbrook, Massachusetts.<br>&nbsp;Since 1972 we have taken pride<br>in our quality, craftsmanship and<br>attention to detail in the art of<br>building, renovations and historic<br>restoration. As a team<br>we help our clients create<br>projects that exceed<br>their expectations.</p>

  <div class="brand">
    <div class="brand-name"><span class="brand-mark"></span>HollowbrookJoinery</div>
    <div class="brand-tagline">cabinetry &amp; interior finish</div>
  </div>

  <h1 class="greeting">Hi I'm Owen</h1>

  <p class="about">We have been doing all sorts of quality carpentry, woodworking and built-ins around Boston for a number of years. We know that homeowners want quality and affordability that will look great and last. We also know that this is a rare combination. So we decided to feature some of our work on this site and invite you to contact us for a free estimate.</p>

  <p class="offer">If you have a spot in the house that deserves some special treatment, we can help.<br>Get affordable custom built-ins for your home.<br>You'll be thrilled with the results.</p>

  <p class="contact">
    <span class="contact-lead">Please Call or email for more information and a free estimate.<br>Place your order for Custom Doors and Drawers.</span>
    Owen Marsh<br>
    555 - 014 - 2271<br>
    owen@hollowbrookjoinery.example<br>
    http://www.hollowbrookjoinery.example/
  </p>
</main>
</body>
</html>
```